Pizza Restaurant Needs a New Menu Design

RESTAURANT NAME: The Oven and Barrel House
LOCATION:
- Kyneton, central Victoria Australia
- A small historical country town, with a growing market in visitors from Melbourne coming for food and local activities.
TYPE OF RESTAURANT
Pizza and Pasta restaurant. Modern feel, lots of timber, busy feel.
- Describe the overall restaurant theme/concept
- Ambiance
CLIENTELE:
- Mostly local clientele, but a growing number of tourists also. Local families and young people.
Describe your patrons or your market
OBJECTIVE:
-to give a more modern and professional feel to our menus. They are old and simple and boring.
- hard to read under low light at night.
Why are we updating the old menu?
- What do you like about the old menu that designers should keep or consider when designing
- What do you not like about the old menu?
ADDITIONAL INFORMATION:
www.ovenandbarrelhouse.com.au
https://www.facebook.com/The-Oven-and-Barrel-House-804417362958120/
RESOURCES/ SIZES:
Please find attached all our current menus as requested. With all attachments you will notice 2 of everything. We currently print each menu back to back on white card.
Restaurant 1 and Restaurant 2 - back to back - A3 and then folded
Red Wine and White Wine - back to back A4
Take away 1 and Take away 2 - back to back A4
Dessert - A4 - cut in half
Lunch Menu and Lunch Drink Menu - back to back A4
A3 Takeaway Menu
Thank you :)

```html
<!DOCTYPE html>
<html lang="en">
<head>
<meta charset="utf-8">
<title>Dessert Menu</title>
<link rel="stylesheet" href="https://fonts.googleapis.com/css2?family=Montserrat:wght@800&family=PT+Sans:ital,wght@0,700;1,400&display=swap">
<style>
  :root {
    --crimson: #b01b40;
    --timber: #f2e4c4;
    --timber-deep: #e9d3a8;
    --panel: #ffffff;
    --ink: #1f1f1f;
    --ink-soft: #3d2224;
    --note: #5a2a2c;
    --blush: #f6e8ec;
    --blush-deep: #eecbd3;
    --ornament: #d8637f;
  }
  html, body { margin: 0; padding: 0; overflow: hidden; }
  body { width: 848px; height: 1200px; }
  .menu-sheet {
    position: relative; width: 848px; height: 1200px; overflow: hidden;
    background: linear-gradient(135deg, var(--timber), var(--timber-deep));
  }
  .frame-band { position: absolute; background: var(--crimson); }
  .frame-band.top { left: 0; top: 0; width: 848px; height: 14px; }
  .frame-band.left { left: 0; top: 0; width: 8px; height: 1200px; }
  .frame-band.bottom { left: 0; top: 1182px; width: 848px; height: 18px; }
  .leaf-accent { position: absolute; background: rgba(255,255,255,0.75); border-radius: 50% 50% 0 0; }
  .leaf-accent.one { left: 330px; top: 0; width: 80px; height: 14px; }
  .leaf-accent.two { left: 730px; top: 0; width: 90px; height: 14px; }
  .panel {
    position: absolute; left: 8px; top: 14px; width: 800px; height: 1102px;
    background: var(--panel); overflow: hidden;
  }
  .backdrop { position: absolute; left: 0; top: 0; width: 848px; height: 1200px; }
  .menu-half { position: absolute; top: 0; width: 400px; height: 700px; }
  .menu-half.first { left: 0; }
  .menu-half.second { left: 432px; width: 368px; }
  .menu-title {
    position: absolute; left: 50px; top: 22px; margin: 0; white-space: nowrap;
    font: 800 17px/1 "Montserrat", sans-serif; color: #111;
  }
  .menu-note {
    position: absolute; left: 70px; top: 52px; margin: 0; white-space: nowrap;
    font: italic 400 18px/1 "PT Sans", sans-serif; color: var(--note);
  }
  .second .menu-title { left: 9px; top: 24px; }
  .second .menu-note { left: 16px; top: 53px; }
  .divider {
    position: absolute; left: 21px; width: 345px; height: 5px; border-radius: 3px;
    background: linear-gradient(90deg, var(--ornament), #eaa6b7, var(--ornament));
    opacity: 0.75;
  }
  .divider.upper { top: 98px; }
  .divider.lower { left: 32px; top: 642px; width: 346px; }
  .second .divider.upper { left: 9px; }
  .second .divider.lower { left: 19px; }
  .item-name, .item-desc { position: absolute; margin: 0; white-space: nowrap; }
  .item-name { font: 700 16px/20px "PT Sans", sans-serif; color: var(--ink); }
  .item-desc { font: italic 400 14px/18px "PT Sans", sans-serif; color: var(--ink-soft); }
</style>
</head>
<body>
<div class="menu-sheet">
  <div class="frame-band top"></div>
  <div class="frame-band left"></div>
  <div class="leaf-accent one" role="img" aria-label="White leaf flourish"></div>
  <div class="leaf-accent two" role="img" aria-label="White leaf flourish"></div>

  <div class="panel">
    <svg class="backdrop" viewBox="0 0 848 1200" aria-hidden="true">
      <path d="M0 778 C 110 770, 210 820, 270 900 C 330 980, 380 1060, 430 1110 L0 1110 Z" fill="var(--blush)"/>
    </svg>

    <section class="menu-half first">
      <h1 class="menu-title">DESSERT MENU</h1>
      <p class="menu-note">Desserts are made in-house</p>
      <div class="divider upper" role="img" aria-label="Decorative scroll divider"></div>

      <h2 class="item-name" style="left:78px;top:146px">STICKY DATE PUDDING - $8.00</h2>
      <p class="item-desc" style="left:44px;top:173px">with butterscotch sauce, cream and/ or ice cream</p>

      <h2 class="item-name" style="left:89px;top:226px">APPLE CRUMBLE - $8.00</h2>
      <p class="item-desc" style="left:42px;top:253px">Juicy apples slices baked with crumble,</p>
      <p class="item-desc" style="left:130px;top:270px">topped with cream and/ or ice cream</p>

      <h2 class="item-name" style="left:81px;top:329px">CHOCOLATE MOUSSE - $8.00</h2>
      <p class="item-desc" style="left:41px;top:358px">Rich creamy chocolate mousse served with cream</p>

      <h2 class="item-name" style="left:30px;top:417px">ICE CREAM SUNDAE - $8.00 (KIDS SIZE - $6.00)</h2>
      <p class="item-desc" style="left:53px;top:449px">Scoops of Vanilla Ice cream served with</p>
      <p class="item-desc" style="left:118px;top:466px">choice of topping</p>
      <p class="item-desc" style="left:53px;top:483px">Chocolate, Strawberry or Caramel (Sprinkles optional )</p>

      <h2 class="item-name" style="left:86px;top:534px">ICE CREAM CONE - $2.00</h2>
      <p class="item-desc" style="left:32px;top:564px">Scoop of Vanilla Ice Cream in a cone (sprinkles optional)</p>

      <div class="divider lower" role="img" aria-label="Decorative scroll divider"></div>
    </section>

    <section class="menu-half second">
      <h1 class="menu-title">DESSERT MENU</h1>
      <p class="menu-note">Desserts are made in-house</p>
      <div class="divider upper" role="img" aria-label="Decorative scroll divider"></div>

      <h2 class="item-name" style="left:78px;top:147px">STICKY DATE PUDDING - $8.00</h2>
      <p class="item-desc" style="left:41px;top:174px">with butterscotch sauce, cream and/ or ice cream</p>

      <h2 class="item-name" style="left:96px;top:227px">APPLE CRUMBLE - $8.00</h2>
      <p class="item-desc" style="left:38px;top:254px">Juicy apples slices baked with crumble,</p>
      <p class="item-desc" style="left:127px;top:271px">topped with cream and/ or ice cream</p>

      <h2 class="item-name" style="left:88px;top:330px">CHOCOLATE MOUSSE - $8.00</h2>
      <p class="item-desc" style="left:48px;top:359px">Rich creamy chocolate mousse served with cream</p>

      <h2 class="item-name" style="left:38px;top:418px">ICE CREAM SUNDAE - $8.00 (KIDS SIZE - $6.00)</h2>
      <p class="item-desc" style="left:60px;top:450px">Scoops of Vanilla Ice cream served with</p>
      <p class="item-desc" style="left:126px;top:467px">choice of topping</p>
      <p class="item-desc" style="left:60px;top:484px">Chocolate, Strawberry or Caramel (Sprinkles optional )</p>

      <h2 class="item-name" style="left:94px;top:535px">ICE CREAM CONE - $2.00</h2>
      <p class="item-desc" style="left:26px;top:565px">Scoop of Vanilla Ice Cream in a cone (sprinkles optional)</p>

      <div class="divider lower" role="img" aria-label="Decorative scroll divider"></div>
    </section>
  </div>

  <svg class="backdrop" viewBox="0 0 848 1200" aria-hidden="true" style="pointer-events:none">
    <path d="M0 1112 C 120 1100, 220 1120, 260 1182 L0 1182 Z" fill="var(--blush-deep)"/>
    <path d="M700 1182 C 740 1150, 800 1130, 848 1130 L848 1182 Z" fill="#e6c7a4"/>
  </svg>
  <div class="frame-band bottom"></div>
</div>
</body>
</html>
```